原稿及び詳細の指定は、添付資料(ほしかげチラシ原稿、及び サービスの流れ)をご確認下さい。

また、今まで使用していたチラシのデータ(.ai形式)及び、当社で作成していたイラスト(わずかですが・・・)も添付致しました。
作成頂く際に、都合のよいものがありましたら、ご自由にご利用して頂いても結構です。
※この素材の雰囲気に合わせたチラシを作成してほしい、ということではありません。

キャラクターに関しても取り出してご使用いただいても、一部改変して使用して頂いても(もちろん使用しなくても)構いません。
お手数ですが、添付資料をご覧ください。
A4
両面
お任せします。
現在、同サービスのランディングページを当サイトで募集をかけ選定中です。
そのランディングページの内容を凝縮したのが、今回のチラシです。
よろしければ、参考にご覧下さい。

『彩光ITケアのランディングページ※デザインのみ』http://www.tsumugiba.jp/work/detail/58172
現在、多忙の為、選定が遅れてしまっております。

来週を目処に、何名かのツムギスト様に修正依頼等
お願いさせて頂く予定でおります。

ツムギストの皆様にはご迷惑をお掛けしておりますが、
何卒宜しくお願い申し上げます。

デザインの親しみやすさと、
文章量の多い原稿を、煩雑にならない程度に見やすくレイアウトして頂いているのが好印象でした。

この度、ご提案いただきました皆様には深く御礼申し上げます。

今回はお選び出来なかった皆様のご提案も大変興味深いものでした。
また、機会がございましたらぜひともよろしくお願い申し上げます。

```html
<!DOCTYPE html>
<html lang="ja">
<head>
<meta charset="utf-8">
<title>ほしかげ パソコン調査サービス</title>
<link href="https://fonts.googleapis.com/css2?family=M+PLUS+Rounded+1c:wght@400;700;800&family=Noto+Sans+JP:wght@400;700&display=swap" rel="stylesheet">
<style>
:root{
  --sky:#d9f0fb;
  --sky-deep:#7ccbed;
  --green:#6cbf3a;
  --green-dark:#3f8e1f;
  --lime:#d8ef7a;
  --blue:#2d8fd8;
  --orange:#f08a1c;
  --red:#e2231a;
  --ink:#333;
  --muted:#666;
  --paper:#fff;
  --yellow:#fff45c;
}
*{box-sizing:border-box;margin:0;padding:0}
html,body{width:849px;height:1200px;overflow:hidden;background:#fff}
body{font-family:"Noto Sans JP",sans-serif;color:var(--ink);font-size:11px}
.flyer{position:relative;width:849px;height:1200px;background:linear-gradient(#e6f6fd,#fff 30%);overflow:hidden}

.pack-title{position:absolute;left:20px;top:10px;width:560px;height:38px;border-radius:19px;background:var(--green);color:#fff;font:800 21px "M PLUS Rounded 1c",sans-serif;line-height:38px;padding-left:22px}
.mascot{position:absolute;border-radius:50%;background:radial-gradient(circle at 40% 40%,#fff36a,#f1c618)}

.packs{position:absolute;left:14px;top:56px;width:821px;display:flex;gap:10px}
.pack{flex:1;background:#fff;border:2px solid var(--sky-deep);border-radius:10px;height:132px;position:relative;overflow:hidden}
.pack h3{font:800 20px/1.1 "M PLUS Rounded 1c",sans-serif;text-align:center;margin-top:10px}
.pack h3 small{display:block;font-size:15px}
.pack.basic h3{color:var(--green-dark)}
.pack.mail h3{color:var(--blue)}
.pack.full h3{color:var(--orange)}
.chips{position:absolute;right:10px;top:44px;display:flex;gap:3px}
.chip{width:30px;height:30px;border-radius:50%;background:var(--lime);font-size:7px;font-weight:700;display:flex;align-items:center;justify-content:center;text-align:center;line-height:1.1;color:var(--green-dark)}
.chip.b{background:#bfe3fa;color:var(--blue)}
.chip.o{background:#ffd9a8;color:var(--orange)}
.price{position:absolute;left:0;right:0;bottom:0;height:46px;background:var(--yellow);color:var(--red);font:800 32px/46px "M PLUS Rounded 1c",sans-serif;text-align:center}
.pack.full .price{height:60px;line-height:34px;font-size:30px}
.finance{position:absolute;left:10px;bottom:4px;font:800 14px "M PLUS Rounded 1c",sans-serif;color:var(--ink)}
.finance b{background:var(--orange);color:#fff;padding:0 4px;border-radius:3px}
.finance span{color:var(--muted);font-size:12px;margin-left:40px}

.visit-title{position:absolute;left:22px;top:196px;font:800 18px "M PLUS Rounded 1c",sans-serif;color:var(--green-dark)}
.visit-title em{font-style:normal;color:var(--red)}
.visit{position:absolute;left:22px;top:222px;width:805px;height:50px;font:700 14px "M PLUS Rounded 1c",sans-serif}
.visit .row{position:absolute;white-space:nowrap}
.visit .row b{color:var(--red);font-size:15px}
.visit .row.big b{font-size:19px}
.plus{position:absolute;left:272px;top:0;width:50px;height:48px;background:var(--orange);color:#fff;border-radius:8px;font-size:11px;text-align:center;line-height:1.2;padding-top:9px}

.flow-bar{position:absolute;left:20px;top:278px;width:600px;height:22px;border-radius:11px;background:var(--green);color:#fff;font:800 14px/22px "M PLUS Rounded 1c",sans-serif;padding-left:18px}
.flow{position:absolute;left:20px;top:304px;width:809px;height:52px;display:flex;align-items:center;gap:8px}
.art{border-radius:8px;background:linear-gradient(#cde9f7,#9fd2ee)}
.step{height:34px;border-radius:17px;background:#fff;border:2px solid var(--green);font:800 15px/30px "M PLUS Rounded 1c",sans-serif;padding:0 16px;color:var(--green-dark)}
.arrow{width:0;height:0;border-left:14px solid var(--orange);border-top:10px solid transparent;border-bottom:10px solid transparent}

.examples{position:absolute;left:14px;top:360px;width:821px;height:340px;background:#bde3f5;border-radius:10px;padding:6px}
.examples h2{text-align:center;font:800 15px "M PLUS Rounded 1c",sans-serif;color:#fff;background:var(--blue);border-radius:8px;height:22px;line-height:22px;margin-bottom:6px}
.cols{display:flex;gap:6px}
.col{flex:1;background:#fff;border-radius:8px;overflow:hidden;height:300px}
.col header{color:#fff;font:800 15px "M PLUS Rounded 1c",sans-serif;text-align:center;padding:4px 0 2px}
.col header strong{display:block;font-size:30px;line-height:1.1}
.col.file header{background:var(--orange)}
.col.mail header{background:var(--blue)}
.col.net header{background:var(--green)}
.col ul{list-style:none;padding:10px 12px;font-size:10.5px;line-height:1.6;color:var(--ink)}
.col li{margin-bottom:8px}
.col li::before{content:"・"}

.pricelist{position:absolute;left:20px;top:710px;width:809px;display:flex;gap:14px;font-size:11.5px;font-weight:700}
.pricelist dl{flex:1;display:grid;grid-template-columns:1fr auto;row-gap:4px}
.pricelist dt::before{content:"■";color:var(--blue);margin-right:2px}
.pricelist dd{color:var(--red)}
.pricelist dt.tag::before{color:var(--orange)}
.note{position:absolute;left:20px;top:830px;font-size:11px;color:var(--muted)}

.footer{position:absolute;left:14px;top:854px;width:821px;height:336px;border:2px solid var(--green);border-radius:10px;background:#fff}
.footer .label{position:absolute;left:0;top:0;background:var(--green);color:#fff;font:800 13px "M PLUS Rounded 1c",sans-serif;padding:3px 12px;border-radius:8px 0 8px 0}
.brand{position:absolute;left:20px;top:40px;display:flex;align-items:center;gap:8px;font:800 32px "M PLUS Rounded 1c",sans-serif;color:var(--green-dark)}
.brand i{width:26px;height:26px;border-radius:50%;background:var(--yellow);display:block}
.contact{position:absolute;left:200px;top:30px;width:400px}
.contact .svc{display:inline-block;background:var(--sky);color:var(--blue);font-weight:700;font-size:12px;padding:2px 10px;border-radius:10px}
.tel{display:flex;align-items:center;gap:6px;font:800 38px "M PLUS Rounded 1c",sans-serif;color:var(--blue);margin-top:4px}
.hours{font-size:11px;color:var(--muted);line-height:1.6}
.company{position:absolute;left:20px;top:150px;width:580px;font-size:11px;color:var(--muted);line-height:1.6}
.memo{position:absolute;left:620px;top:30px;width:180px;height:290px;border-left:1px dashed #bbb;padding-left:12px;font-weight:700;font-size:12px;color:var(--green-dark)}
.memo span{display:block;border-bottom:1px dotted #bbb;height:34px}
</style>
</head>
<body>
<main class="flyer">
  <div class="pack-title">用途に合わせたお得な3つのパック</div>
  <div class="mascot" role="img" aria-label="黄色い小鳥のキャラクター" style="left:600px;top:4px;width:44px;height:44px"></div>

  <section class="packs">
    <article class="pack basic">
      <h3>基本お調べ<small>パック</small></h3>
      <div class="chips"><span class="chip">ウィルス<br>チェック</span><span class="chip">ファイル<br>総合調査</span></div>
      <div class="price">¥19,800</div>
    </article>
    <article class="pack mail">
      <h3>メールお調べ<small>パック</small></h3>
      <div class="chips"><span class="chip b">ウィルス<br>チェック</span><span class="chip b">ファイル<br>総合調査</span><span class="chip b">メール<br>調査</span></div>
      <div class="price">¥29,800</div>
    </article>
    <article class="pack full">
      <h3>まるごとお調べ<small>パック</small></h3>
      <div class="chips"><span class="chip o">ウィルス</span><span class="chip o">ファイル</span><span class="chip o">メール</span><span class="chip o">ネット</span></div>
      <div class="price">¥44,800</div>
      <div class="finance"><b>金融</b>取引調査<span>＋¥19,800</span></div>
    </article>
  </section>

  <div class="visit-title">ご訪問とセットでお得なサービス <em>ご訪問料金込みで、ラクチン！安心！</em></div>
  <div class="visit">
    <div class="row" style="left:0;top:2px">■ パソコン簡易診断 <b>¥4,980</b></div>
    <div class="row" style="left:0;top:26px">■ パスワード解析 <b>¥14,700</b></div>
    <div class="plus">ご訪問<br>プラス</div>
    <div class="row big" style="left:340px;top:0">■ ご訪問パソコン簡易診断 <b>¥9,800</b></div>
    <div class="row big" style="left:340px;top:24px">■ ご訪問パスワード解析 <b>¥9,800</b></div>
  </div>

  <div class="flow-bar">サービスの流れ</div>
  <div class="flow">
    <div class="art" role="img" aria-label="相談するスタッフと利用者のイラスト" style="width:110px;height:50px"></div>
    <div class="step">無料ご相談</div><div class="arrow"></div>
    <div class="art" role="img" aria-label="パソコンを調べるスタッフのイラスト" style="width:110px;height:50px"></div>
    <div class="step">ご依頼のサービス</div><div class="arrow"></div>
    <div class="art" role="img" aria-label="報告書を渡すスタッフのイラスト" style="width:110px;height:50px"></div>
    <div class="step">ご報告</div>
  </div>

  <section class="examples">
    <h2>ご利用例</h2>
    <div class="cols">
      <div class="col file">
        <header>ファイル総合調査<strong>¥26,250</strong></header>
        <ul>
          <li>故人のパソコンにどんなデータが残っているか知りたい。</li>
          <li>写真や文書を探して整理し、家族で分けて保存したい。</li>
          <li>パソコン内の膨大なデータから必要な書類や写真を探し出し、一覧にしてお渡しします。</li>
          <li>消えてしまったファイルの確認もご相談ください。</li>
        </ul>
      </div>
      <div class="col mail">
        <header>メール調査<strong>¥15,750</strong></header>
        <ul>
          <li>メールが大事な連絡先のヒントになるかもしれない。</li>
          <li>知人や取引先への連絡を漏れなく行いたい。</li>
          <li>大量のメールの中から必要な相手先やメッセージを抜き出し、整理してご報告します。</li>
          <li>契約やサービスの手がかりも探します。</li>
        </ul>
      </div>
      <div class="col net">
        <header>インターネット利用調査<strong>¥18,600</strong></header>
        <ul>
          <li>故人が利用していたサイトやサービスを知りたい。</li>
          <li>サイトのIDやパスワードが分からず解約できない。</li>
          <li>閲覧履歴や登録情報から利用中のサービスを調べ、各種SNSなど解約に必要な情報をまとめます。</li>
        </ul>
      </div>
    </div>
  </section>

  <section class="pricelist">
    <dl>
      <dt>写真ピックアップサービス</dt><dd>¥6,300</dd>
      <dt>データ消去サービス</dt><dd>¥6,300</dd>
      <dt>パスワード解析</dt><dd>¥14,700</dd>
      <dt>データ復元サービス</dt><dd>¥18,900</dd>
      <dt>パソコン簡易診断</dt><dd>¥4,980</dd>
    </dl>
    <dl>
      <dt>コピー調査</dt><dd>¥12,600</dd>
      <dt>パソコン調査</dt><dd>¥6,300</dd>
      <dt>パソコン修理</dt><dd>¥8,400</dd>
      <dt>パソコン処分</dt><dd>¥3,150</dd>
      <dt class="tag">お急ぎ料金</dt><dd>¥5,250</dd>
    </dl>
    <dl>
      <dt>パソコンデータ完全消去</dt><dd>¥2,100</dd>
      <dt>パソコン初期化</dt><dd>¥2,100</dd>
      <dt>パソコンクリーニング</dt><dd>¥2,100</dd>
      <dt>ウィルスチェック</dt><dd>¥2,100</dd>
      <dt>出張料金</dt><dd>¥2,100</dd>
    </dl>
  </section>
  <p class="note">※その他、ファイルプリント、ウィルスチェックなどもご相談ください。</p>

  <section class="footer">
    <div class="label">ご相談窓口</div>
    <div class="brand"><i></i>ほしかげ</div>
    <div class="contact">
      <span class="svc">パソコン調査サービス ほしかげ</span>
      <div class="tel">
        <svg width="34" height="34" viewBox="0 0 24 24" aria-hidden="true"><path fill="#2d8fd8" d="M6.6 10.8a15 15 0 0 0 6.6 6.6l2.2-2.2c.3-.3.7-.4 1-.2 1.1.4 2.3.6 3.6.6.6 0 1 .4 1 1V20c0 .6-.4 1-1 1A17 17 0 0 1 3 4c0-.6.4-1 1-1h3.5c.6 0 1 .4 1 1 0 1.3.2 2.5.6 3.6.1.3 0 .7-.2 1z"/></svg>
        0120-468-219
      </div>
      <p class="hours">受付時間 10:00〜18:00（土・日・祝日を除く）</p>
    </div>
    <p class="company">（運営会社）ミナモ企画株式会社<br>〒150-0000 東京都渋谷区星見町1-2-3</p>
    <div class="memo">お問い合わせ控え<span></span><span></span><span></span><span></span><span></span><span></span><span></span></div>
  </section>
</main>
</body>
</html>
```